Redesign my business cards

I would like pretty much all the same information as my current business cards but redesigned to stand out more and be more unique photo uploaded to show my current business cards don’t mind if you want to remove or replace I for on the back

```html
<!DOCTYPE html>
<html lang="en">
<head>
<meta charset="utf-8">
<title>Vantree Detailing – Business Card</title>
<link href="https://fonts.googleapis.com/css2?family=Michroma&family=Montserrat:wght@400;600&display=swap" rel="stylesheet">
<style>
  :root {
    --backdrop: #979797;
    --aqua: #2adcdc;
    --blue: #5688e6;
    --mid-blue: #3f9ad9;
    --heading: #3a7fd0;
    --body-text: #6d6d6d;
    --rule: #c8c8c8;
    --white: #ffffff;
  }
  * { box-sizing: border-box; margin: 0; padding: 0; }
  html, body { width: 1200px; height: 1000px; overflow: hidden; }
  body { background: var(--backdrop); position: relative; font-family: "Montserrat", sans-serif; }

  .card {
    position: absolute;
    left: 293px;
    width: 614px;
    height: 350px;
    border-radius: 30px;
    overflow: hidden;
  }

  .card-front {
    top: 109px;
    background: linear-gradient(90deg, var(--aqua) 0%, var(--mid-blue) 55%, var(--blue) 100%);
    display: flex;
    align-items: center;
    justify-content: center;
  }
  .brand-mark {
    display: flex;
    flex-direction: column;
    align-items: center;
    gap: 14px;
    color: var(--white);
    font-family: "Michroma", sans-serif;
    text-align: center;
  }
  .brand-dot { width: 14px; height: 14px; border-radius: 50%; background: var(--white); }
  .brand-name { font-size: 30px; letter-spacing: 8px; line-height: 1.35; }

  .card-back { top: 510px; background: var(--white); }
  .splash-area { position: absolute; left: 0; top: 0; width: 614px; height: 82px; }

  .service { position: absolute; top: 100px; }
  .service-interior { left: 23px; width: 162px; }
  .service-exterior { left: 222px; width: 175px; }
  .service-full { left: 430px; width: 166px; top: 95px; }
  .service-title {
    font-family: "Michroma", sans-serif;
    color: var(--heading);
    font-size: 13.5px;
    line-height: 16px;
    letter-spacing: 0.5px;
    margin-bottom: 5px;
  }
  .service-text { color: var(--body-text); font-size: 11.7px; line-height: 14.5px; letter-spacing: 0.3px; }

  .divider { position: absolute; left: 23px; top: 282px; width: 566px; height: 1px; background: var(--rule); }

  .owner { position: absolute; left: 23px; top: 295px; }
  .owner-name { font-family: "Michroma", sans-serif; color: var(--heading); font-size: 12.5px; letter-spacing: 0.3px; }
  .owner-role { font-family: "Michroma", sans-serif; font-variant: small-caps; color: var(--body-text); font-size: 10px; margin-top: 2px; }

  .contact { position: absolute; left: 222px; top: 292px; font-family: "Michroma", sans-serif; color: var(--body-text); }
  .contact-row { display: flex; align-items: center; gap: 8px; height: 19px; }
  .contact-phone { font-size: 13px; letter-spacing: 1.2px; }
  .contact-email { font-size: 10.5px; letter-spacing: 0.6px; text-transform: uppercase; }
  .contact-row svg { flex: none; }
</style>
</head>
<body>

<section class="card card-front">
  <div class="brand-mark">
    <span class="brand-dot"></span>
    <div class="brand-name">VANTREE<br>DETAILING</div>
  </div>
</section>

<section class="card card-back">
  <svg class="splash-area" viewBox="0 0 614 82" role="img" aria-label="Blue water splash decoration">
    <defs>
      <linearGradient id="splashFill" x1="0" y1="0" x2="1" y2="0">
        <stop offset="0" stop-color="#5688e6"/>
        <stop offset="0.7" stop-color="#4aa6df"/>
        <stop offset="1" stop-color="#2adedb"/>
      </linearGradient>
    </defs>
    <path d="M0,0 H614 V78 C480,40 330,82 200,70 C110,62 50,50 0,40 Z" fill="url(#splashFill)"/>
  </svg>

  <article class="service service-interior">
    <h2 class="service-title">INTERIOR<br>DETAIL</h2>
    <p class="service-text">Vacume &amp; deep clean of carpets &amp; upholstery or leather treatment, interior trim clean &amp; condition, window polish and treatment, steam clean and stain removal</p>
  </article>
  <article class="service service-exterior">
    <h2 class="service-title">EXTERIOR<br>DETAIL</h2>
    <p class="service-text">Extreme wash &amp; polish, exterior trim reviver &amp; protector window polish &amp; treatment, tyre dressing, engine bay cleaned.</p>
  </article>
  <article class="service service-full">
    <h2 class="service-title">FULL EXTREME<br>DETAIL</h2>
    <p class="service-text">Extreme wash &amp; polish, tyre dressing, engine bay cleaned, vacume &amp; deep clean of carpets &amp; upholstery or leather treatment, interior &amp; exterior trim reviver &amp; protector, window polish and treatment.</p>
  </article>

  <div class="divider"></div>

  <div class="owner">
    <div class="owner-name">OWEN HALBROOK</div>
    <div class="owner-role">Owner/ Operator</div>
  </div>

  <div class="contact">
    <div class="contact-row contact-phone">
      <svg width="10" height="14" viewBox="0 0 10 14" aria-hidden="true"><rect x="1" y="0.5" width="8" height="13" rx="1.5" fill="none" stroke="#3a7fd0" stroke-width="1.3"/><circle cx="5" cy="11" r="0.9" fill="#3a7fd0"/></svg>
      <span>0412550176</span>
    </div>
    <div class="contact-row contact-email">
      <svg width="12" height="9" viewBox="0 0 12 9" aria-hidden="true"><rect width="12" height="9" fill="#3a7fd0"/><path d="M0,0 L6,5 L12,0" fill="none" stroke="#fff" stroke-width="1"/></svg>
      <span>vantreedetailing@example.com</span>
    </div>
  </div>
</section>

</body>
</html>
```